National commercial insurance agency needs design for email campaign to other insurance agencies ...

National commercial insurance agency needs design for email campaign to other insurance agencies needing to place workers comp policies and and also need very intense risk management. We want to market to smaller insurance agencies to refer us to their larger clients or prospects.

Font styles to use
Sans Serif

```html
<!DOCTYPE html>
<html lang="en">
<head>
<meta charset="utf-8">
<title>Veranta — We Have You Surrounded</title>
<link rel="stylesheet" href="https://fonts.googleapis.com/css2?family=Quicksand:wght@500;700&family=Mulish:wght@400;600;700&family=Poppins:wght@400&display=swap">
<style>
  :root {
    --orange: #f26c37;
    --ink: #111111;
    --text: #5a5a5a;
    --nav: #555555;
    --band-grey: #606060;
    --header-bg: #f2f2f2;
    --footer-bg: #000000;
    --white: #ffffff;
  }
  * { margin: 0; padding: 0; box-sizing: border-box; }
  html, body { width: 1200px; height: 2812px; overflow: hidden; background: var(--white); }
  body { position: relative; font-family: "Mulish", sans-serif; color: var(--text); }

  .site-header { position: absolute; left: 0; top: 0; width: 1200px; height: 118px; background: var(--header-bg); }
  .brand { position: absolute; left: 84px; top: 9px; width: 285px; height: 100px; background: var(--white);
    display: flex; align-items: center; justify-content: center; gap: 14px; }
  .brand-name { font-family: "Quicksand", sans-serif; font-weight: 700; font-size: 44px; color: #3c3c3c; }
  .brand-dot { width: 30px; height: 30px; border-radius: 50%; background: var(--orange); }
  .main-nav { position: absolute; top: 42px; left: 634px; display: flex; gap: 0; }
  .main-nav a { font-family: "Poppins", sans-serif; font-size: 26px; color: var(--nav); text-decoration: none; position: absolute; white-space: nowrap; }
  .main-nav a:nth-child(1) { left: 0; }
  .main-nav a:nth-child(2) { left: 206px; }
  .main-nav a:nth-child(3) { left: 371px; }

  .hero { position: absolute; left: 0; top: 118px; width: 1200px; height: 632px; }
  .hero-photo { position: absolute; inset: 0; background: linear-gradient(160deg, #5a6e8a 0%, #33476a 40%, #24355a 70%, #6b5a4a 100%); }
  .hero-cut { position: absolute; left: 0; top: 0; }
  .hero-title { position: absolute; left: 0; right: 0; top: 272px; text-align: center; font-family: "Quicksand", sans-serif;
    font-weight: 700; font-size: 66px; color: var(--white); }

  .mission-title { position: absolute; left: 0; right: 0; top: 845px; text-align: center; font-family: "Quicksand", sans-serif;
    font-weight: 700; font-size: 56px; color: var(--ink); }
  .pillar { position: absolute; top: 992px; width: 240px; text-align: center; }
  .pillar-icon { display: block; margin: 0 auto; width: 184px; height: 184px; }
  .pillar-label { margin-top: 34px; font-family: "Quicksand", sans-serif; font-weight: 700; font-size: 35px; color: var(--ink); }

  .section-band { position: absolute; left: 0; }
  .band-orange { top: 1378px; }
  .band-title { position: absolute; left: 51px; top: 1398px; font-family: "Mulish", sans-serif; font-weight: 600; font-size: 42px; color: var(--white); }
  .hr-copy { position: absolute; left: 56px; top: 1512px; width: 1010px; font-family: Arial, Helvetica, sans-serif;
    font-size: 25px; line-height: 48px; color: #444; }

  .band-grey { top: 1808px; }
  .band-heading { position: absolute; left: 50px; top: 1828px; width: 820px; font-weight: 700; font-size: 33px; line-height: 49px; color: var(--white); }

  .agency-copy { position: absolute; left: 47px; top: 2000px; width: 640px; font-family: "Mulish", sans-serif;
    font-size: 27.5px; line-height: 48px; color: var(--text); }
  .team-photo { position: absolute; left: 701px; top: 2008px; width: 475px; height: 630px;
    background: linear-gradient(180deg, #c9d0d6 0%, #8d959c 45%, #4b5560 100%); }

  .site-footer { position: absolute; left: 0; top: 2709px; width: 1200px; height: 103px; background: var(--footer-bg);
    display: flex; align-items: center; justify-content: center; font-family: "Quicksand", sans-serif; font-weight: 500;
    font-size: 29px; color: var(--white); }
</style>
</head>
<body>
  <header class="site-header">
    <div class="brand"><span class="brand-name">VERANTA</span><span class="brand-dot"></span></div>
    <nav class="main-nav">
      <a href="#">Our Expertise</a>
      <a href="#">Resources</a>
      <a href="#">Contact</a>
    </nav>
  </header>

  <section class="hero">
    <div class="hero-photo" role="img" aria-label="Two smiling warehouse workers in hard hats and blue overalls, one holding a clipboard, between stocked shelves"></div>
    <svg class="hero-cut" width="1200" height="632" viewBox="0 0 1200 632">
      <polygon points="0,529 938,632 1200,529 1200,632 0,632" fill="#ffffff"/>
    </svg>
    <h1 class="hero-title">We Have You Surrounded</h1>
  </section>

  <h2 class="mission-title">Our Mission</h2>

  <div class="pillar" style="left:180px">
    <svg class="pillar-icon" viewBox="0 0 184 184">
      <circle cx="92" cy="92" r="92" fill="var(--orange)"/>
      <g fill="none" stroke="#fff" stroke-width="5" stroke-linejoin="round">
        <polygon points="92,42 140,68 92,94 44,68"/>
        <polyline points="44,88 92,114 140,88"/>
        <polyline points="44,108 92,134 140,108"/>
      </g>
    </svg>
    <div class="pillar-label">Compliance</div>
  </div>

  <div class="pillar" style="left:480px">
    <svg class="pillar-icon" viewBox="0 0 184 184">
      <circle cx="92" cy="92" r="92" fill="var(--orange)"/>
      <g fill="none" stroke="#fff" stroke-width="5" stroke-linejoin="round">
        <line x1="44" y1="134" x2="140" y2="134"/>
        <rect x="52" y="108" width="16" height="26"/>
        <rect x="76" y="94" width="16" height="40"/>
        <rect x="100" y="80" width="16" height="54"/>
        <polyline points="52,96 76,76 96,86 122,56"/>
        <polyline points="110,54 124,52 124,66"/>
      </g>
    </svg>
    <div class="pillar-label">Profit Leaks</div>
  </div>

  <div class="pillar" style="left:780px">
    <svg class="pillar-icon" viewBox="0 0 184 184">
      <circle cx="92" cy="92" r="92" fill="var(--orange)"/>
      <g fill="none" stroke="#fff" stroke-width="5" stroke-linejoin="round">
        <path d="M56 42 H104 L122 60 V112 M122 138 H56 Z" />
        <line x1="56" y1="42" x2="56" y2="138"/>
        <polyline points="104,42 104,60 122,60"/>
        <line x1="70" y1="72" x2="108" y2="72"/>
        <line x1="70" y1="88" x2="108" y2="88"/>
        <line x1="70" y1="104" x2="100" y2="104"/>
        <circle cx="124" cy="130" r="16"/>
        <line x1="124" y1="121" x2="124" y2="132"/>
        <line x1="124" y1="137" x2="124" y2="139"/>
      </g>
    </svg>
    <div class="pillar-label">Claims</div>
  </div>

  <svg class="section-band band-orange" width="520" height="96" viewBox="0 0 520 96">
    <polygon points="0,0 512,0 422,96 0,96" fill="var(--orange)"/>
  </svg>
  <h3 class="band-title">HR Services</h3>
  <p class="hr-copy">Nemo enim ipsam voluptatem quia voluptas sit aspernatur aut odit aut fugit, sed quia consequuntur magni dolores eos qui ratione voluptatem sequi nesciunt. Neque porro quisquam est, qui dolorem ipsum quia dolor sit amet, consectetur, adipisci velit, sed quia non numquam eius modi tempora incidunt ut labore et dolore magnam aliquam quaerat voluptatem.</p>

  <svg class="section-band band-grey" width="945" height="144" viewBox="0 0 945 144">
    <polygon points="0,0 941,0 844,144 0,144" fill="var(--band-grey)"/>
  </svg>
  <h3 class="band-heading">Who can do it all-from handbooks to managing your Human Resource Department</h3>

  <p class="agency-copy">Our agency model is very different than most agencies. We believe in the value of specialization and we specialize in one area. Helping employers mitigate their workers comp costs. With our team of experienced work comp professionals and our proven programs and strategies, we correct and control the specific claims and profit leaks that drive work comp premiums. After a very scientific analysis of an employer’s risk, Veranta designs a customized program for each client that consisting human resource consulting, safety training and compliance, claims management, analytics and audit representation.</p>
  <div class="team-photo" role="img" aria-label="Three smiling office professionals in business attire standing together, arms crossed"></div>

  <footer class="site-footer">© 2019 Copyrights | All Rights Reserved</footer>
</body>
</html>
```